Mural painter needs a Fun, Artistic, Text based design

I am painting a mural at a Marina.
They need the entite "Mission Statement" painted on the wall in a fun creative way. The only color is Dark Blue text on a white wall.
Because it is for a Marina, where they have boats, It would be fun to have a person on skis or a boat run through the center and distort the text.

I am attaching a template of the wall. The "focal point is the center between the two doors.
I am also attaching several ideas we like for inspiration!

Here is what they want written on the wall....
We need to write ALL 4 of the following text in the design....
................................................................
MAKE IT TOGETHER
Do what has never been done…together.

MAKE IT RIGHT
Honor your faith and your word.

MAKE IT HAPPEN
Roll up your sleeves and get the job done.

MAKE IT FUN
Be the reason someone smiles today.

Target Market(s)

Co workers

Industry/Entity Type

Boat, marina, water sports

Font styles to use
Other font styles liked:
• Variety of different BOLD fonts

Colors
0054AA
0677BA
7BADD7
CADEEF
E8F1F8

Requirements
Must have
• Please Use the wall template that I provided. The design must fit on the wall and must include ALL 4 of the phrases, not just one phrase.. I will be painting the design mural on the wall. Fun playful text design, different fonts
Nice to have
• Possibly a boat or person skiing in the center. Keep this detail small. The main idea is the text.. just thought it would look neat if the boat went over the text and the words were distorted slightly. Just an idea.
Should not have
• Only dark blue and possibly a touch of Gold color

```html
<!DOCTYPE html>
<html lang="en">
<head>
<meta charset="utf-8">
<title>Marina Mission Mural – Wall Elevation</title>
<link rel="stylesheet" href="https://fonts.googleapis.com/css2?family=Archivo+Black&family=Bangers&family=Comic+Neue:wght@700&family=Gochi+Hand&family=Lilita+One&family=Passion+One:wght@700&display=swap">
<style>
  :root {
    --navy: #0d2554;
    --door: #80857e;
    --wall: #ffffff;
    --line: #000000;
    --water-light: #e8f1f8;
    --water-mid: #cadeef;
  }
  * { margin: 0; padding: 0; box-sizing: border-box; }
  html, body { width: 1200px; height: 900px; overflow: hidden; background: #fff; }
  .canvas { position: relative; width: 1200px; height: 900px; }

  .wall {
    position: absolute; left: 61px; top: 302px; width: 1088px; height: 397px;
    border: 2px solid var(--line); background: var(--wall);
  }
  .door {
    position: absolute; top: 372px; width: 111px; height: 327px;
    background: var(--door); border: 3px solid var(--line); border-bottom: none;
  }
  .door--left { left: 95px; }
  .door--right { left: 822px; }

  .dimension {
    position: absolute; left: 490px; top: 714px; width: 100px; text-align: center;
    font-family: "Archivo Black", sans-serif; font-style: italic; font-size: 38px; color: var(--line);
  }

  .line { position: absolute; white-space: nowrap; color: var(--navy); line-height: 1; }

  .headline-together {
    left: 290px; top: 354px; width: 440px; text-align: center;
    font-family: "Bangers", sans-serif; font-size: 68px;
    transform: skewX(-8deg);
  }
  .tagline { font-family: "Comic Neue", sans-serif; font-weight: 700; font-size: 17px; }
  .tagline--together { left: 302px; top: 412px; width: 400px; text-align: center; font-size: 20px; }

  .headline-right {
    top: 428px;
    font-family: "Lilita One", sans-serif; font-size: 54px;
    color: var(--wall); -webkit-text-stroke: 2px var(--navy);
    text-shadow: 3px 3px 0 var(--navy);
  }
  .headline-right--left { left: 282px; }
  .headline-right--right { left: 526px; }

  .script { font-family: "Gochi Hand", cursive; font-size: 25px; }
  .script--faith { left: 293px; top: 475px; }
  .script--word { left: 548px; top: 475px; }

  .headline-happen { top: 500px; font-family: "Passion One", sans-serif; font-weight: 700; font-size: 54px; }
  .headline-happen--left { left: 282px; }
  .headline-happen--right { left: 549px; }

  .tagline--sleeves { left: 278px; top: 548px; }
  .tagline--done { left: 578px; top: 548px; }

  .headline-fun { top: 566px; font-family: "Archivo Black", sans-serif; font-size: 44px; }
  .headline-fun--left { left: 263px; }
  .headline-fun--right { left: 597px; }

  .script--reason { left: 255px; top: 606px; font-size: 24px; }
  .script--smiles { left: 595px; top: 607px; font-size: 22px; letter-spacing: -1px; }

  .jetski-art { position: absolute; left: 472px; top: 470px; width: 72px; height: 168px; }
  .bubbles { position: absolute; left: 0; top: 0; width: 1200px; height: 900px; pointer-events: none; }
  .bubbles circle { fill: var(--navy); }
</style>
</head>
<body>
<main class="canvas">
  <div class="wall"></div>
  <div class="door door--left"></div>
  <div class="door door--right"></div>

  <section class="mural" aria-label="Mission statement mural">
    <p class="line headline-together">MAKE IT TOGETHER</p>
    <p class="line tagline tagline--together">Do what has never been done…together.</p>

    <p class="line headline-right headline-right--left">MAKE IT</p>
    <p class="line headline-right headline-right--right">RIGHT</p>
    <p class="line script script--faith">Honor your faith</p>
    <p class="line script script--word">and your word.</p>

    <p class="line headline-happen headline-happen--left">MAKE IT</p>
    <p class="line headline-happen headline-happen--right">HAPPEN</p>
    <p class="line tagline tagline--sleeves">Roll up your sleeves</p>
    <p class="line tagline tagline--done">and get the job done..</p>

    <p class="line headline-fun headline-fun--left">MAKE</p>
    <p class="line headline-fun headline-fun--right">IT FUN</p>
    <p class="line script script--reason">Be the reason</p>
    <p class="line script script--smiles">someone smiles today.</p>

    <svg class="jetski-art" viewBox="0 0 72 168" preserveAspectRatio="none" role="img" aria-label="Line illustration of a rider on a jet ski cutting through splashing water">
      <defs>
        <linearGradient id="water" x1="0" y1="0" x2="0" y2="1">
          <stop offset="0" stop-color="#e8f1f8"/>
          <stop offset="1" stop-color="#cadeef"/>
        </linearGradient>
      </defs>
      <rect width="72" height="168" fill="url(#water)"/>
    </svg>

    <svg class="bubbles" viewBox="0 0 1200 900" aria-hidden="true">
      <circle cx="262" cy="422" r="7"/><circle cx="281" cy="421" r="6.5"/><circle cx="270" cy="407" r="4"/><circle cx="285" cy="407" r="2"/>
      <circle cx="252" cy="466" r="5"/><circle cx="267" cy="467" r="5.5"/><circle cx="259" cy="477" r="3.5"/><circle cx="247" cy="475" r="1.5"/><circle cx="259" cy="496" r="2"/>
      <circle cx="248" cy="510" r="5"/><circle cx="269" cy="509" r="8"/><circle cx="257" cy="527" r="8"/>
      <circle cx="733" cy="411" r="5"/><circle cx="748" cy="413" r="5.5"/><circle cx="740" cy="423" r="3"/><circle cx="728" cy="423" r="1.5"/>
      <circle cx="732" cy="454" r="8"/><circle cx="755" cy="456" r="9"/><circle cx="741" cy="473" r="5"/><circle cx="724" cy="470" r="2"/>
      <circle cx="748" cy="512" r="5"/><circle cx="765" cy="506" r="2"/><circle cx="765" cy="524" r="7.5"/><circle cx="743" cy="534" r="7"/>
    </svg>
  </section>

  <p class="dimension">17’</p>
</main>
</body>
</html>
```